Startup fashion company needs high-end, stylish and hip business cards!

We need a business card design that uses a logo that we just completed with a SketchHive artist.

Our company is Velmora. We work with fashion designers to display their designs on our website and handle all back-end fulfillment for them (fabric sourcing, garment manufacturing, customer service, etc.). The word Velmora is a play on fashion trunk shows, where designers will show their wares in a small, intimate setting. The final design should communicate high-end / luxe, chic, stylish, fashion-forward, hip!

We are using greys as our logo color (#2d2d2d, #ababab). We are also interested, for branding purposes and on our website, to use purple as a highlight color (#4a3455). I have the logo in other formats if needed.

Target Market(s)

Investors, customers, fashion designers, suppliers

Industry/Entity Type

Fashion

Contact Information for Business Card

There should be space for:
Name
Title
Address 1
Address 2
City, State Zip
USA
Phone
Email
Skype
Twitter

If it makes sense to put one or more of the contact info on the same line, that is fine if it won't be confusing.

Font styles to use
Sans Serif
Other font styles liked:
• Would like the font to be complementary to our logo font/look and feel. The logo font is Caviar Dreams with a stylized 'N' according to the logo designer.

Colors
876aae
e4daea
f3f1f8
ffffff

Requirements
Must have
• The cards will most likely printed through PrintNova and therefore must meet their upload file guidelines. There are also software templates for business cards that can be utilized. Information below from PrintNova site.
• We support a variety of file formats for uploaded designs.
• Adobe Acrobat 9 Document (*.pdf) (recommended)
• Adobe Illustrator CS3 Artwork (*.ai) (recommended)
• Adobe Photoshop CS3 Image (*.psd) (recommended)
• Bitmap Image (*.bmp)
• GIF Image (*.gif)
• JPEG Image (*.jpg,*.jpeg)
• Microsoft PowerPoint 2010 Document (*.ppt)
• Microsoft Publisher 2010 Document (*.pub)
• Microsoft Word 2010 Document (*.doc)
• PCX Image (*.pcx)
• PICT Image (*.pic,*.pict,*.pct)
• PNG Image (*.png)
• PostScript Document (*.ps)
• TIFF Image (*.tif,*.tiff)
• Windows Enhanced Metafile (*.emf)
• Windows Metafile (*.wmf)
• The templates on their site:
• Using a downloadable template for your application will ensure that your dimensions, resolution and color settings match ours.
• If you are creating a PDF document in Acrobat Distiller, please use our Distiller settings.
• Sizing:
• Full Bleed Size
• 3.62" x 2.12"
• 92 x 54 mm
• 1085 x 635 pixels
• Document Trim Size
• 3.50" x 2.00"
• 89 x 51 mm
• 1050 x 600 pixels
Nice to have
• The back can use either the full logo or just the elephant or a combination? I'm imagining a full color backside...open to other suggestions!

```html
<!DOCTYPE html>
<html lang="en">
<head>
<meta charset="utf-8">
<title>Velmora business cards</title>
<link rel="stylesheet" href="https://fonts.googleapis.com/css2?family=Questrial&family=Montserrat:wght@700&display=swap">
<style>
  :root {
    --purple: #4a3455;
    --ink: #2d2d2d;
    --grey: #ababab;
    --white: #ffffff;
    --page: #eceaef;
  }
  * { margin: 0; padding: 0; box-sizing: border-box; }
  html, body { width: 1200px; height: 900px; overflow: hidden; background: var(--page); }
  .canvas { position: relative; width: 1200px; height: 900px; }

  .card {
    position: absolute; left: 250px; width: 700px; height: 400px;
    border-radius: 22px; overflow: hidden;
    box-shadow: 0 6px 18px rgba(0,0,0,0.18);
  }

  /* back */
  .card-back { top: 30px; background: var(--purple); }
  .back-brand {
    position: absolute; left: 70px; top: 140px;
    font-family: "Questrial", sans-serif; color: var(--white);
  }
  .back-brand .wordmark { font-size: 40px; letter-spacing: 4px; line-height: 1; }
  .back-brand .web { font-size: 14px; letter-spacing: 3px; margin-top: 8px; }
  .emblem-area { position: absolute; right: 0; top: 0; width: 330px; height: 400px; }
  .emblem-area svg { display: block; width: 100%; height: 100%; }

  /* front */
  .card-front { top: 470px; background: var(--white); }
  .side-band { position: absolute; left: 40px; top: 0; width: 42px; height: 100%; background: var(--purple); }
  .brand-mark {
    position: absolute; left: 29px; top: 16px; width: 64px; height: 64px;
    border-radius: 50%; background: var(--purple); border: 4px solid var(--white);
  }
  .front-wordmark {
    position: absolute; left: 106px; top: 22px;
    font-family: "Questrial", sans-serif; font-size: 60px; letter-spacing: 5px;
    color: var(--ink); line-height: 1;
  }
  .contact-list {
    position: absolute; left: 40px; top: 112px; list-style: none;
    font-family: "Questrial", sans-serif; font-size: 16px; color: var(--ink);
  }
  .contact-list li { display: flex; align-items: center; height: 23px; }
  .contact-list .icon { width: 42px; display: flex; justify-content: center; }
  .contact-list .icon svg { width: 13px; height: 13px; }
  .contact-list .text { padding-left: 18px; white-space: nowrap; }

  .person { position: absolute; right: 44px; bottom: 40px; text-align: right; font-family: "Montserrat", sans-serif; font-weight: 700; }
  .person .name { font-size: 24px; color: var(--ink); }
  .person .title { font-size: 16px; color: var(--purple); margin-top: 2px; }
</style>
</head>
<body>
<main class="canvas">

  <section class="card card-back">
    <div class="back-brand">
      <div class="wordmark">VELMORA</div>
      <div class="web">www.velmora-studio.com</div>
    </div>
    <div class="emblem-area" role="img" aria-label="Large brand emblem in white on the purple back">
      <svg viewBox="0 0 330 400" preserveAspectRatio="none">
        <path d="M120 400 C120 300 150 170 230 90 C270 50 310 30 330 25 L330 400 Z" fill="#ffffff"/>
      </svg>
    </div>
  </section>

  <section class="card card-front">
    <div class="side-band"></div>
    <div class="brand-mark"></div>
    <div class="front-wordmark">VELMORA</div>

    <ul class="contact-list">
      <li><span class="icon"><svg viewBox="0 0 12 12"><path d="M6 0.5a3.8 3.8 0 0 0-3.8 3.8C2.2 7 6 11.5 6 11.5S9.8 7 9.8 4.3A3.8 3.8 0 0 0 6 0.5z" fill="#fff"/><circle cx="6" cy="4.3" r="1.4" fill="#4a3455"/></svg></span><span class="text">Suite 210 Linden Avenue</span></li>
      <li><span class="icon"></span><span class="text">New York, NY 10012, USA</span></li>
      <li><span class="icon"><svg viewBox="0 0 12 12"><path d="M1 3.5C1 2 2 1.5 6 1.5s5 .5 5 2v1H8.5V3.2h-5v1.3H1z M2.5 5.5h7l1 5h-9z" fill="#fff"/></svg></span><span class="text">212 555 0148</span></li>
      <li><span class="icon"><svg viewBox="0 0 12 12"><rect x="0.5" y="2.5" width="11" height="7.5" fill="#fff"/><path d="M0.8 2.8 6 6.8l5.2-4" stroke="#4a3455" stroke-width="1" fill="none"/></svg></span><span class="text">info@velmora-studio.com</span></li>
      <li><span class="icon"><svg viewBox="0 0 12 12"><circle cx="6" cy="6" r="5.5" fill="#fff"/></svg></span><span class="text">Velmora</span></li>
      <li><span class="icon"><svg viewBox="0 0 12 12"><rect x="0.5" y="0.5" width="11" height="11" fill="#fff"/></svg></span><span class="text">Velmora</span></li>
      <li><span class="icon"><svg viewBox="0 0 12 12"><circle cx="6" cy="6" r="5.2" fill="none" stroke="#fff" stroke-width="1"/><ellipse cx="6" cy="6" rx="2.3" ry="5.2" fill="none" stroke="#fff" stroke-width="1"/><path d="M0.8 6h10.4M1.6 3.5h8.8M1.6 8.5h8.8" stroke="#fff" stroke-width="0.8"/></svg></span><span class="text">www.velmora-studio.com</span></li>
    </ul>

    <div class="person">
      <div class="name">Jordan Hale</div>
      <div class="title">Director</div>
    </div>
  </section>

</main>
</body>
</html>
```